" O nome Valtessora significa dentro do movimento. A clínica tem como carro chefe um trabalho chamado de videoanálise de movimento. Usamos um software para realizar análise de marcha, corrida, salto, estabilidade, flexibilidade entre outros. Identificamos alteraçoes no movimento que possam ser a causa de dor ou diminmuiçao no rendimento físico-funcional. Alteraçoes identificadas entramos com a reabilitaçao usando Pilates, RPG, Hidroterapia, Treinamento Funcional, Osteopatia entre outros. Nosso foco: resultados! "

```html
<!DOCTYPE html>
<html lang="pt-BR">
<head>
<meta charset="UTF-8">
<title>Valtessora — Cartão de Visita</title>
<link href="https://fonts.googleapis.com/css2?family=Ubuntu:wght@400;500&display=swap" rel="stylesheet">
<style>
  :root {
    --bg: #e4e5e8;
    --card-light: #f6f9fe;
    --card-mid: #dfe8f8;
    --card-deep: #b7cbee;
    --ink: #2a4a9a;
    --ink-soft: #5b79c0;
    --mark-light: #c9d8f3;
    --mark-mid: #7f9fdc;
    --mark-deep: #2f4fa3;
  }
  * { margin: 0; padding: 0; box-sizing: border-box; }
  html, body {
    width: 1200px;
    height: 1200px;
    overflow: hidden;
    background: var(--bg);
    font-family: "Ubuntu", sans-serif;
  }
  .card {
    position: absolute;
    border-radius: 72px;
    overflow: hidden;
    background: linear-gradient(150deg, var(--card-light) 0%, var(--card-mid) 55%, var(--card-deep) 100%);
  }
  .card-front {
    left: 115px;
    top: 60px;
    width: 881px;
    height: 509px;
  }
  .card-back {
    left: 228px;
    top: 612px;
    width: 864px;
    height: 449px;
  }
  .brand {
    position: absolute;
    left: 0;
    right: 0;
    top: 150px;
    display: flex;
    flex-direction: column;
    align-items: center;
  }
  .brand-dot {
    width: 72px;
    height: 72px;
    border-radius: 50%;
    background: var(--ink);
    margin-bottom: 34px;
  }
  .brand-name {
    font-weight: 500;
    font-size: 70px;
    line-height: 1;
    color: var(--ink);
    letter-spacing: -1px;
  }
  .brand-tagline {
    margin-top: 8px;
    font-weight: 400;
    font-size: 17px;
    letter-spacing: 3px;
    color: var(--ink-soft);
  }
  .back-decoration {
    position: absolute;
    left: 0;
    top: 0;
    width: 460px;
    height: 100%;
    background:
      radial-gradient(ellipse 40% 18% at 45% 22%, var(--mark-deep) 0%, transparent 100%),
      radial-gradient(ellipse 45% 38% at 50% 58%, var(--mark-mid) 0%, var(--mark-light) 60%, transparent 100%);
    opacity: 0.85;
  }
  .holder-name {
    position: absolute;
    left: 487px;
    top: 102px;
    font-size: 27px;
    font-weight: 400;
    color: var(--ink);
  }
  .contact {
    position: absolute;
    left: 487px;
    top: 298px;
    font-size: 19px;
    line-height: 24px;
    color: var(--ink);
    list-style: none;
  }
</style>
</head>
<body>
  <section class="card card-front">
    <div class="brand">
      <span class="brand-dot"></span>
      <span class="brand-name">Valtessora</span>
      <span class="brand-tagline">Centro de Análise do Movimento</span>
    </div>
  </section>

  <section class="card card-back">
    <div class="back-decoration" role="img" aria-label="Grande elemento decorativo em tons de azul com curvas em movimento"></div>
    <p class="holder-name">Nome Sobrenome</p>
    <ul class="contact">
      <li>Endereço&nbsp; Onono non nono, 999</li>
      <li>Cep: 99999-99 - Nononono- NO</li>
      <li>Fone: (99) 9999-9999</li>
      <li>contato@valtessora.com</li>
      <li>www.valtessora.com</li>
    </ul>
  </section>
</body>
</html>
```